Heron Renovation Group Postcard Design Project

I'm a General Contractor specializing in luxury residential remodeling.

THIS IS AN EDDM POSTCARD. THE ENTIRE BACK SIDE OF THE CARD WILL BE USED.

I FORGOT TO MENTION THIS IN MY ORIGINAL BRIEF.

Target Market(s)

OLD, rich people so please make sure the fonts are clear and crisp.

Font styles to use
Sans Serif

```html
<!DOCTYPE html>
<html lang="en">
<head>
<meta charset="utf-8">
<title>Heron Renovation Group – EDDM Postcard</title>
<link href="https://fonts.googleapis.com/css2?family=Montserrat:wght@800&family=Roboto:wght@400;500&family=Roboto+Condensed:ital,wght@1,300&display=swap" rel="stylesheet">
<style>
  :root{
    --stage:#6e6e6e;
    --red:#e02727;
    --charcoal:#2f2f30;
    --charcoal-dark:#252526;
    --white:#ffffff;
    --ink:#1d1d1d;
    --soft:#d8d8d8;
  }
  *{box-sizing:border-box;margin:0;padding:0}
  html,body{width:1200px;height:1200px;overflow:hidden;background:var(--stage)}
  body{position:relative;font-family:"Roboto",Arial,sans-serif}
  .side-label{position:absolute;color:var(--white);font-size:38px;font-weight:400;line-height:1}
  .side-label--front{left:550px;top:594px}
  .side-label--back{left:368px;top:1084px}

  /* FRONT */
  .card-front{position:absolute;left:78px;top:45px;width:416px;height:614px;background:var(--white);overflow:hidden}
  .card-front__brand{position:absolute;top:28px;left:0;right:0;display:flex;justify-content:center;align-items:center;gap:6px;
    font-family:"Roboto",Arial,sans-serif;font-weight:500;font-size:13px;color:var(--red);letter-spacing:.3px}
  .brand-mark{width:10px;height:10px;background:var(--red);border-radius:50%}
  .card-front__photo{position:absolute;left:0;top:70px;width:416px;height:260px;
    background:linear-gradient(180deg,#fff 0%,#c9cbe8 18%,#8f98c9 40%,#9c8e80 60%,#c7b8a2 72%,#4f7a36 88%,#3f6a2a 100%)}
  .card-front__panel{position:absolute;left:0;top:0;width:416px;height:614px}
  .headline{position:absolute;left:0;right:0;top:347px;text-align:center;color:var(--white);
    font-family:"Montserrat",Arial,sans-serif;font-weight:800;font-size:29px;line-height:33px}
  .divider{position:absolute;left:108px;width:210px;top:485px;height:1px;background:#8b8b8b}
  .contractor-name{position:absolute;left:0;right:0;top:493px;text-align:center;color:var(--white);font-size:21px;font-weight:400}
  .contractor-role{position:absolute;left:0;right:0;top:520px;text-align:center;color:var(--white);
    font-family:"Roboto Condensed",Arial,sans-serif;font-style:italic;font-weight:300;font-size:21px}
  .contact-band{position:absolute;left:0;bottom:0;width:416px;height:56px;background:var(--red);color:var(--white);
    font-size:16.5px;text-align:center;padding-top:6px;line-height:20px}
  .contact-band svg{vertical-align:-2px;margin-right:4px}

  /* BACK */
  .card-back{position:absolute;left:494px;top:706px;width:618px;height:418px;background:var(--white);overflow:hidden}
  .card-back svg.back-art{position:absolute;left:0;top:0}
  .services{position:absolute;left:20px;top:232px;list-style:none;color:var(--white);font-size:14.5px;line-height:18px}
  .services li{display:flex;align-items:center;gap:7px}
  .license{position:absolute;left:35px;top:294px;width:228px;height:17px;border:1px solid #cfcfcf;color:var(--white);
    font-size:12.5px;line-height:15px;text-align:center}
  .value{position:absolute;color:var(--white);font-size:12.5px;line-height:13px}
  .values-hub{position:absolute;left:80px;top:345px;width:164px;height:26px;border-radius:50%;background:var(--red);
    border:1px solid #fff;color:var(--white);font-size:13px;font-weight:500;text-align:center;line-height:24px}
  .mail-brand{position:absolute;left:386px;top:18px;display:flex;align-items:center;gap:4px;color:var(--red);font-size:8px;font-weight:500}
  .mail-brand .brand-mark{width:7px;height:7px}
  .mail-contact{position:absolute;left:386px;top:45px;font-size:7px;line-height:9px;color:var(--ink)}
  .stamp-box{position:absolute;left:551px;top:11px;width:40px;height:37px;background:#bdbdbd}
  .address-line{position:absolute;left:432px;width:159px;height:1.5px;background:var(--ink)}
</style>
</head>
<body>

<section class="card-front" aria-label="Postcard front">
  <div class="card-front__photo" role="img" aria-label="Photo of a large two-storey luxury home with lit windows at dusk and a green lawn"></div>
  <div class="card-front__brand"><span class="brand-mark"></span>Heron Renovation Group</div>
  <svg class="card-front__panel" viewBox="0 0 416 614" aria-hidden="true">
    <polygon points="0,291 208,321 416,291 416,614 0,614" fill="var(--red)"/>
    <polygon points="0,302 208,330 416,302 416,614 0,614" fill="var(--charcoal)"/>
  </svg>
  <h1 class="headline">Remodeling Luxury<br>Homes &amp; Building<br>Lasting Relationships<br>Since 1995</h1>
  <div class="divider"></div>
  <p class="contractor-name">Daniel Heron</p>
  <p class="contractor-role">General Contractor</p>
  <div class="contact-band">
    <div><svg width="14" height="14" viewBox="0 0 16 16"><circle cx="8" cy="8" r="7" fill="none" stroke="#fff" stroke-width="1.3"/><path d="M5.5 4.5l1.3 1.6-.8 1a5 5 0 0 0 2.9 2.9l1-.8 1.6 1.3-.8 1.1c-3 0-5.9-2.9-5.9-5.9z" fill="#fff"/></svg>480-555-0142</div>
    <div><svg width="14" height="14" viewBox="0 0 16 16"><circle cx="8" cy="8" r="7" fill="none" stroke="#fff" stroke-width="1.2"/><ellipse cx="8" cy="8" rx="3" ry="7" fill="none" stroke="#fff" stroke-width="1"/><line x1="1" y1="8" x2="15" y2="8" stroke="#fff"/></svg>www.HeronRenovationGroup.com</div>
  </div>
</section>
<span class="side-label side-label--front">Front</span>

<section class="card-back" aria-label="Postcard back">
  <svg class="back-art" width="618" height="418" viewBox="0 0 618 418">
    <defs>
      <linearGradient id="backPhoto" x1="0" y1="0" x2="0" y2="1">
        <stop offset="0" stop-color="#e4e6e6"/>
        <stop offset=".3" stop-color="#c89a4c"/>
        <stop offset=".55" stop-color="#b5853e"/>
        <stop offset=".75" stop-color="#56703a"/>
        <stop offset="1" stop-color="#3e5a2c"/>
      </linearGradient>
      <linearGradient id="backShade" x1="0" y1="0" x2="0" y2="1">
        <stop offset="0" stop-color="#333" stop-opacity="0"/>
        <stop offset=".25" stop-color="#333" stop-opacity=".95"/>
        <stop offset="1" stop-color="var(--charcoal-dark)"/>
      </linearGradient>
      <linearGradient id="circlePhoto" x1="0" y1="0" x2="0" y2="1">
        <stop offset="0" stop-color="#4c7fd0"/>
        <stop offset=".5" stop-color="#d9a37a"/>
        <stop offset="1" stop-color="#3f9a2c"/>
      </linearGradient>
    </defs>
    <g role="img" aria-label="Photo of a tan Mediterranean-style two-storey villa with tiled roofs and palm trees">
      <polygon points="0,0 386,0 330,150 394,418 0,418" fill="url(#backPhoto)"/>
    </g>
    <polygon points="0,200 345,200 394,418 0,418" fill="url(#backShade)"/>
    <polygon points="386,0 396,0 340,150 404,418 394,418 330,150" fill="var(--red)"/>
    <circle cx="324" cy="196" r="44" fill="var(--red)"/>
    <circle cx="324" cy="196" r="41" fill="url(#circlePhoto)" role="img" aria-label="Photo of an open hand holding a small model house over grass"/>
    <g stroke="#d0d0d0" stroke-width="1">
      <line x1="84" y1="332" x2="240" y2="370"/>
      <line x1="90" y1="360" x2="250" y2="360"/>
      <line x1="72" y1="394" x2="240" y2="348"/>
      <line x1="232" y1="330" x2="85" y2="372"/>
      <line x1="262" y1="362" x2="78" y2="358"/>
      <line x1="254" y1="394" x2="92" y2="348"/>
    </g>
  </svg>

  <ul class="services">
    <li><svg width="11" height="10" viewBox="0 0 11 10"><path d="M1 5.5l3 3L10 1" fill="none" stroke="#fff" stroke-width="2"/></svg>All Phases of Residential Remodeling</li>
    <li><svg width="11" height="10" viewBox="0 0 11 10"><path d="M1 5.5l3 3L10 1" fill="none" stroke="#fff" stroke-width="2"/></svg>Partial &amp; Large Scale Renovations</li>
    <li><svg width="11" height="10" viewBox="0 0 11 10"><path d="M1 5.5l3 3L10 1" fill="none" stroke="#fff" stroke-width="2"/></svg>Complimentary Design Services</li>
  </ul>
  <div class="license">Licensed / Bonded / Insured #508314</div>

  <span class="value" style="left:34px;top:320px">Integrity</span>
  <span class="value" style="left:18px;top:338px">The<br>Creative<br>Process</span>
  <span class="value" style="left:23px;top:381px">Having<br>Fun</span>
  <span class="value" style="left:236px;top:316px">Educating Our<br>Clients</span>
  <span class="value" style="left:268px;top:348px">Quality<br>Craftsmanship</span>
  <span class="value" style="left:258px;top:381px">World Class<br>Customer Service</span>
  <div class="values-hub">Our Core Values</div>

  <div class="mail-brand"><span class="brand-mark"></span>Heron Renovation Group</div>
  <div class="mail-contact">480-555-0142<br>www.HeronRenovationGroup.com</div>
  <div class="stamp-box"></div>
  <div class="address-line" style="top:209px"></div>
  <div class="address-line" style="top:231px"></div>
  <div class="address-line" style="top:257px"></div>
</section>
<span class="side-label side-label--back">Back</span>

</body>
</html>
```